Consulting firm needs elegant, modern designs

Business card design - I have a logo which has previously been developed for Q-Pathways - I will attach. I will also attach specifications for the size of the business card.

We also need a logo design for our leadership consulting product - Form in Guidance - we focus on improving workplace health by educating leaders and learning professionals about how the physical and emotional affects performance and engagement. I have some example logos and ideas which I will attach - these have attempted to bring in the body but I do not like the font (see www.formingguidance-example.com for preferred font). Idea is to please have a 'body' visible somehow in the word Leadership, ensuring that this conveys flexibility and agility. Colors which I prefer are deep purple OR turquoise, together with silver. COLORS below are for LOGO design.

Target Market(s)

For the business card, it should be more masculine. The logo which will be attached should be neutralized into dark blue shades and silver. The business card Q-Pathways is focused on business transformation - organizations who would require a consultant to help them enter new markets, for example.

Industry/Entity Type

Leadership

Contact Information for Business Card

Content:
Q-Pathways
Lindenkade 27
4921KP, Breda, The Netherlands
maurits@Q-Pathways.example
www.Q-Pathways.example

Colors for business card should be conservative and slightly more masculine. Use the Q-Pathways logo but change the colors to blue or shades of gray/black.

Dimensions for cut
85 x 55 mm
1004 x 650 pixels
Full document size
88 x 58 mm
1040 x 685 pixels
For the best result, you need to design the full document size including the bleed

Logo Text

Form in Guidance

Font styles to use
Serif
Sans Serif

Colors
876aae
333333
959595

Requirements
Must have
• Professional, modern and unique business card design
• Professional, elegant, and modern logo design - with creative thinking
Should not have
• Too many colors

```html
<!DOCTYPE html>
<html lang="en">
<head>
<meta charset="UTF-8">
<title>Q-Pathways Business Card</title>
<link rel="stylesheet" href="https://fonts.googleapis.com/css2?family=Lato:wght@400;700&family=Montserrat:wght@300;600&family=Oswald:wght@600&display=swap">
<style>
  :root {
    --page-bg: #2b2b2b;
    --card-bg: #1d1d1e;
    --ink: #f2f2f2;
    --ink-soft: #cfcfcf;
    --accent: #8a6cc4;
    --mark-blue: #3d5fa8;
  }
  * { box-sizing: border-box; margin: 0; padding: 0; }
  html, body { width: 1200px; height: 900px; overflow: hidden; }
  body {
    background: var(--page-bg);
    display: flex;
    flex-direction: column;
    align-items: center;
    justify-content: center;
    gap: 34px;
  }
  .card {
    position: relative;
    width: 620px;
    height: 401px;
    background: var(--card-bg);
    color: var(--ink);
    font-family: 'Lato', sans-serif;
  }

  /* Front */
  .brand {
    position: absolute;
    left: 0; right: 0; top: 118px;
    display: flex;
    justify-content: center;
    align-items: center;
    gap: 16px;
  }
  .brand-dot {
    width: 70px; height: 70px;
    border-radius: 50%;
    background: var(--mark-blue);
    flex: none;
  }
  .brand-text { display: flex; flex-direction: column; }
  .brand-name {
    font-family: 'Montserrat', sans-serif;
    font-weight: 600;
    font-size: 44px;
    letter-spacing: 1px;
    line-height: 1;
    color: var(--ink);
  }
  .brand-tagline {
    font-family: 'Montserrat', sans-serif;
    font-weight: 300;
    font-size: 15px;
    letter-spacing: 1px;
    color: var(--ink-soft);
    margin-top: 6px;
  }
  .front-url {
    position: absolute;
    left: 0; right: 0; top: 292px;
    text-align: center;
    font-size: 14px;
    letter-spacing: 2px;
  }

  /* Back */
  .identity {
    position: absolute;
    right: 352px; top: 132px;
    text-align: right;
  }
  .person-name {
    font-family: 'Oswald', sans-serif;
    font-weight: 600;
    font-size: 30px;
    letter-spacing: 1px;
    text-transform: uppercase;
    color: var(--accent);
    line-height: 1.1;
    white-space: nowrap;
  }
  .person-role { font-size: 16px; margin-top: 4px; }
  .divider {
    position: absolute;
    left: 290px; top: 132px;
    width: 2px; height: 70px;
    background: var(--accent);
  }
  .contacts {
    position: absolute;
    left: 312px; top: 138px;
    list-style: none;
    font-size: 14px;
    line-height: 20px;
    white-space: nowrap;
  }
  .contacts li { display: flex; align-items: center; gap: 10px; }
  .contacts svg { width: 12px; height: 12px; color: var(--accent); fill: var(--accent); flex: none; }
  .address {
    position: absolute;
    left: 72px; bottom: 58px;
    font-size: 15px;
    letter-spacing: 0.5px;
  }
</style>
</head>
<body>
  <section class="card card-front">
    <div class="brand">
      <span class="brand-dot"></span>
      <div class="brand-text">
        <span class="brand-name">Q-Pathways</span>
        <span class="brand-tagline">Guiding each new move</span>
      </div>
    </div>
    <p class="front-url">www.Q-Pathways.example</p>
  </section>

  <section class="card card-back">
    <div class="identity">
      <h1 class="person-name">Daniel Verhoef</h1>
      <p class="person-role">Founder</p>
    </div>
    <span class="divider"></span>
    <ul class="contacts">
      <li>
        <svg viewBox="0 0 24 24" aria-hidden="true"><path d="M6.6 10.8a15 15 0 0 0 6.6 6.6l2.2-2.2a1 1 0 0 1 1-.25 11.4 11.4 0 0 0 3.6.57 1 1 0 0 1 1 1V20a1 1 0 0 1-1 1A17 17 0 0 1 3 4a1 1 0 0 1 1-1h3.5a1 1 0 0 1 1 1c0 1.25.2 2.45.57 3.6a1 1 0 0 1-.25 1z"/></svg>
        (555) 014-2290
      </li>
      <li>
        <svg viewBox="0 0 24 24" aria-hidden="true"><path d="M2 5h20v14H2z M2 5l10 8 10-8" fill="none" stroke="currentColor" stroke-width="2.5"/></svg>
        maurits@Q-Pathways.example
      </li>
      <li>
        <svg viewBox="0 0 24 24" aria-hidden="true"><circle cx="12" cy="12" r="10" fill="none" stroke="currentColor" stroke-width="2"/><path d="M2 12h20M12 2c3 3 3 17 0 20M12 2c-3 3-3 17 0 20" fill="none" stroke="currentColor" stroke-width="2"/></svg>
        www.Q-Pathways.example
      </li>
    </ul>
    <p class="address">Lindenkade 27 4921KP, Breda, The Netherlands</p>
  </section>
</body>
</html>
```